Rovilent.com Trucking Company Website

Need a website designed (no content) for a trucking company, specializing in trucking of ocean containers (intermodal Trucking). Heavy emphasis on technology, using latest technology, providing unabated visibility and realtime information.
clean minimalist industrial website
example:
https://www.belquarn.com/

Target Market(s)

Professional Business Consumer corporate and small business

Industry/Entity Type

Trucking Company

Number of Pages Required

5+ page

Requirements
Must have
• Industrial Design, simple informative, for a busy professional to view and get the necessary information with out the distractions.
• Blog Page
• Client Log-In on the front page
• Technology page - showing our intensive investments in technology
Nice to have
• If ANY images included, MUST be USA related. Example if include an image of a truck, ensure its a USA model. Do the research.
• included our business card for sample of Logo
• Doesnt not have to be the same color schemes.
Should not have
• moving images

```html
<!DOCTYPE html>
<html lang="en">
<head>
<meta charset="utf-8">
<title>Rovilent — Home</title>
<link rel="stylesheet" href="https://fonts.googleapis.com/css2?family=Open+Sans:wght@400;600;700&display=swap">
<style>
  :root {
    --brand-blue: #1f5fa6;
    --panel-blue: rgba(33, 104, 180, 0.95);
    --link-blue: #3e8fe0;
    --ink: #2e2e2e;
    --nav-ink: #555;
    --field: #eef0f3;
    --footer: rgba(22, 22, 22, 0.88);
    --footer-ink: #d8d8d8;
    --button: #1c1c1c;
  }
  * { box-sizing: border-box; margin: 0; padding: 0; }
  html, body { width: 1200px; height: 576px; overflow: hidden; }
  body { font-family: "Open Sans", Arial, sans-serif; color: var(--ink); }
  .page { position: relative; width: 1200px; height: 576px; overflow: hidden; }

  .hero-photo {
    position: absolute; inset: 0;
    background:
      linear-gradient(180deg, #9a9a9a 0%, #d6d6d6 30%, #e8e8e8 55%, #bdbdbd 75%, #7d7d7d 100%);
  }

  .brand {
    position: absolute; left: 248px; top: 30px;
    display: flex; align-items: center; gap: 10px;
    font-weight: 700; font-size: 40px; letter-spacing: 2px;
    color: var(--brand-blue);
  }
  .brand-mark { width: 14px; height: 14px; background: var(--brand-blue); }

  .utility {
    position: absolute; right: 245px; top: 17px;
    display: flex; align-items: center; font-size: 12px; font-weight: 600; color: var(--ink);
  }
  .utility-item { display: flex; align-items: center; gap: 6px; padding: 0 7px; border-right: 1px solid #555; line-height: 14px; }
  .utility-item:last-child { border-right: 0; padding-right: 0; }
  .utility svg { width: 10px; height: 10px; fill: #333; }
  .social-dot { width: 8px; height: 8px; border-radius: 50%; background: var(--brand-blue); }
  .social { gap: 7px; }

  .main-nav {
    position: absolute; left: 246px; top: 94px; width: 708px; height: 36px;
    background: #fff; border: 1px solid #cfcfcf;
    display: flex; justify-content: space-around; align-items: center;
    font-size: 13px; text-transform: uppercase; color: var(--nav-ink);
  }
  .nav-link { position: relative; }
  .nav-link.is-active { color: var(--brand-blue); }
  .nav-link.is-active::after {
    content: ""; position: absolute; left: 50%; bottom: -12px; margin-left: -5px;
    border: 5px solid transparent; border-bottom-color: var(--brand-blue); border-top: 0;
  }

  .quick-contact {
    position: absolute; left: 710px; top: 189px; width: 269px; height: 333px;
    background: var(--panel-blue); color: #fff; padding: 0 17px;
  }
  .quick-contact h2 { font-weight: 400; font-size: 20px; margin: 16px 0 0 -1px; }
  .field-label { display: block; font-size: 12px; margin-top: 5px; }
  .quick-contact h2 + .field-label { margin-top: 11px; }
  .field { display: block; width: 234px; height: 30px; background: var(--field); border: 0; margin-top: 4px; }
  .field-message { height: 86px; }
  .submit {
    display: block; margin-top: 9px; width: 85px; height: 26px; border: 0;
    background: var(--button); color: #fff; font: 700 11px "Open Sans", Arial, sans-serif;
  }

  .site-footer {
    position: absolute; left: 0; bottom: 0; width: 1200px; height: 54px;
    background: var(--footer); font-size: 12px; color: var(--footer-ink);
  }
  .copyright { position: absolute; left: 222px; top: 18px; }
  .footer-links { position: absolute; right: 222px; top: 17px; display: flex; gap: 22px; font-size: 13px; font-weight: 600; color: #fff; }
  .footer-link.is-current { color: var(--link-blue); }
  .panel-pointer {
    position: absolute; left: 952px; top: 0;
    border: 6px solid transparent; border-top-color: var(--panel-blue); border-bottom: 0;
  }
</style>
</head>
<body>
<div class="page">
  <div class="hero-photo" role="img" aria-label="Black and white photo of two white box trucks parked in front of a warehouse under a cloudy sky"></div>

  <div class="brand"><span class="brand-mark"></span>ROVILENT</div>

  <div class="utility">
    <span class="utility-item">
      <svg viewBox="0 0 10 10"><path d="M0 2h10v6H0z M0 2l5 3 5-3" stroke="#fff" stroke-width="0.8"/></svg>
      dispatch@rovilent.com
    </span>
    <span class="utility-item">
      <svg viewBox="0 0 10 10"><path d="M2 0l2 2-1 1.5c.8 1.6 2 2.8 3.5 3.5L8 6l2 2-1.5 2C4 9.5.5 6 0 1.5z"/></svg>
      555.014.2290
    </span>
    <span class="utility-item">
      <svg viewBox="0 0 10 10"><circle cx="3" cy="3" r="2.5" fill="none" stroke="#333" stroke-width="1.2"/><path d="M4.5 4.5L9.5 9.5" stroke="#333" stroke-width="1.4"/></svg>
      Login
    </span>
    <span class="utility-item social">
      <span class="social-dot"></span><span class="social-dot"></span><span class="social-dot"></span>
    </span>
  </div>

  <nav class="main-nav">
    <span class="nav-link is-active">Home</span>
    <span class="nav-link">About Us</span>
    <span class="nav-link">Solutions</span>
    <span class="nav-link">Driver Information</span>
    <span class="nav-link">Blog</span>
    <span class="nav-link">Our Technology</span>
    <span class="nav-link">Contact Us</span>
  </nav>

  <form class="quick-contact">
    <h2>Quick Contact</h2>
    <label class="field-label">Name</label>
    <input class="field" type="text">
    <label class="field-label">Email</label>
    <input class="field" type="email">
    <label class="field-label">Message</label>
    <textarea class="field field-message"></textarea>
    <button class="submit" type="button">SUBMIT</button>
  </form>

  <footer class="site-footer">
    <span class="panel-pointer"></span>
    <p class="copyright">Rovilent © 2017 All Rights Reserved</p>
    <div class="footer-links">
      <span class="footer-link">Privacy</span>
      <span class="footer-link">Blog</span>
      <span class="footer-link">Technology</span>
      <span class="footer-link is-current">Quick Contact</span>
    </div>
  </footer>
</div>
</body>
</html>
```